Brightway Haul & Repair Services, are a company that offers a 'one stop shop' pre-move clean up a

I have already selected a logo which I would like on the front of the business cards along with phone numbers, web address and email which are:
0419574302
www.brightwayhaul.com.au
brightwayhaulrepair@mailbox.example

On the back of the card I would like to list some of the types of service we offer (clean - move - repairs/maintenance) which are:
CLEAN - windows, gutters, solar panels, driveways/paths, carpets.
MOVE - Small/medium size house/office moves, large item pick-up & delivery, yard clean-up and removal.
General maintenance and repairs.

I would like the blue logo on a gray background.

Thanks

```html
<!DOCTYPE html>
<html lang="en">
<head>
<meta charset="utf-8">
<title>Brightway Haul &amp; Repair Services – Business Card</title>
<link rel="stylesheet" href="https://fonts.googleapis.com/css2?family=Open+Sans:wght@400;600;700&family=Titillium+Web:wght@700&display=swap">
<style>
  :root {
    --backdrop: #8c4c2c;
    --card: #ffffff;
    --brand-blue: #2a6db6;
    --wave-blue: #1f64ad;
    --wave-light: #7cb8e6;
    --ink: #1b1b1b;
    --white: #ffffff;
  }
  * { box-sizing: border-box; margin: 0; padding: 0; }
  html, body {
    width: 1200px;
    height: 372px;
    overflow: hidden;
  }
  body {
    position: relative;
    background: var(--backdrop);
    font-family: "Open Sans", Arial, sans-serif;
    color: var(--ink);
  }
  .card {
    position: absolute;
    top: 32px;
    width: 546px;
    height: 310px;
    background: var(--card);
    border-radius: 18px;
    overflow: hidden;
  }
  .card--front { left: 38px; }
  .card--back { left: 618px; }

  .brand-name {
    position: absolute;
    top: 62px;
    left: 0;
    width: 100%;
    text-align: center;
    font-family: "Titillium Web", Arial, sans-serif;
    font-weight: 700;
    font-size: 38px;
    line-height: 40px;
    text-transform: uppercase;
    color: var(--brand-blue);
    letter-spacing: 0.5px;
  }

  .contact-list {
    position: absolute;
    top: 178px;
    left: 0;
    width: 100%;
    list-style: none;
    text-align: center;
    font-size: 15px;
    line-height: 22px;
  }
  .contact-list li {
    display: flex;
    justify-content: center;
    align-items: center;
    gap: 6px;
    padding-left: 70px;
  }
  .contact-list .web { letter-spacing: 1px; }
  .contact-icon { width: 11px; height: 11px; flex: none; }

  .wave {
    position: absolute;
    left: 0;
    bottom: 0;
    width: 546px;
    height: 90px;
  }
  .phone {
    position: absolute;
    right: 38px;
    bottom: 22px;
    display: flex;
    align-items: center;
    gap: 6px;
    color: var(--white);
    font-size: 19px;
    letter-spacing: 0.5px;
  }
  .phone svg { width: 16px; height: 16px; }

  .services-title {
    position: absolute;
    top: 184px;
    width: 100%;
    text-align: center;
    color: var(--brand-blue);
    font-weight: 600;
    font-size: 21px;
    letter-spacing: 2px;
  }
  .services-list {
    position: absolute;
    top: 230px;
    width: 100%;
    text-align: center;
    font-weight: 600;
    font-size: 15px;
    line-height: 30px;
  }
  .services-list .bullet { color: var(--brand-blue); margin-right: 4px; }
  .services-list .gap { display: inline-block; width: 18px; }
</style>
</head>
<body>
  <section class="card card--front">
    <h1 class="brand-name">Brightway Haul<br>&amp; Repair Services</h1>
    <ul class="contact-list">
      <li>
        <svg class="contact-icon" viewBox="0 0 12 12"><rect x="0.5" y="2" width="11" height="8" rx="1" fill="#2a6db6"/><path d="M1 3 L6 7 L11 3" stroke="#fff" stroke-width="1.2" fill="none"/></svg>
        <span>brightwayhaulrepair@mailbox.example</span>
      </li>
      <li class="web">
        <svg class="contact-icon" viewBox="0 0 12 12"><circle cx="6" cy="6" r="5.3" fill="#2a6db6"/><path d="M0.7 6 H11.3 M6 0.7 V11.3 M2 3 H10 M2 9 H10" stroke="#fff" stroke-width="0.8"/></svg>
        <span>www.brightwayhaul.com.au</span>
      </li>
    </ul>
    <svg class="wave" viewBox="0 0 546 90" preserveAspectRatio="none" aria-hidden="true">
      <path d="M0 64 C160 74 300 40 546 34 L546 90 L0 90 Z" fill="var(--wave-light)"/>
      <path d="M0 88 C170 84 280 46 546 40 L546 90 L0 90 Z" fill="var(--wave-blue)"/>
      <path d="M0 52 C180 66 310 16 546 22" stroke="var(--ink)" stroke-width="3" fill="none"/>
    </svg>
    <div class="phone">
      <svg viewBox="0 0 16 16"><circle cx="8" cy="8" r="7" fill="none" stroke="#fff" stroke-width="1.2"/><path d="M5.5 4.5 C5 7 7.5 11 10.5 11.5 L11 10 L9.5 9 L8.7 9.8 C7.6 9.2 6.8 8.3 6.3 7.2 L7 6.4 L6.2 4.6 Z" fill="#fff"/></svg>
      <span>0419574302</span>
    </div>
  </section>

  <section class="card card--back">
    <h2 class="brand-name">Brightway Haul<br>&amp; Repair Services</h2>
    <p class="services-title">Services we offer</p>
    <div class="services-list">
      <p><span class="bullet">•</span>Clean<span class="gap"></span><span class="bullet">•</span>Move</p>
      <p><span class="bullet">•</span>General Maintenance And Repairs.</p>
    </div>
  </section>
</body>
</html>
```